Startup Drone Platform Company business card

We are needing a business card design for our employees. We are a startup drone platform. We are looking for a business card that has our logo on one side, with the employee/company details on the opposite side. We are looking for something that is very eye catching, modern, and bold.

Target Market(s)

This will target both drone pilots and drone businesses, along with all the industries that could utilize drone services (aerial video, aerial photos, inspections, 3d mapping, etc).

Industry/Entity Type

Business

```html
<!DOCTYPE html>
<html lang="en">
<head>
<meta charset="utf-8">
<title>Skylane Aerial – Business Card</title>
<link href="https://fonts.googleapis.com/css2?family=Montserrat:wght@500&family=Roboto+Condensed:wght@300;400;700&display=swap" rel="stylesheet">
<style>
  :root {
    --page-bg: #e8e6e3;
    --card-dark: #2e2d31;
    --band-dark: #38373b;
    --card-white: #ffffff;
    --brand-blue: #1c6bbd;
    --accent-teal: #3cbfc7;
    --text-light: #e9e9ea;
    --text-dark: #2e2d31;
  }
  * { margin: 0; padding: 0; box-sizing: border-box; }
  html, body { width: 1200px; height: 891px; overflow: hidden; }
  body { background: var(--page-bg); position: relative; font-family: "Roboto Condensed", sans-serif; }

  .card { position: absolute; box-shadow: 0 10px 28px rgba(0,0,0,.18); }

  /* Front side */
  .card-front {
    left: 80px; top: 274px; width: 600px; height: 343px;
    background: var(--card-dark);
    display: flex; align-items: center; justify-content: center;
  }
  .brand { display: flex; align-items: center; gap: 16px; }
  .brand-dot { width: 18px; height: 18px; border-radius: 50%; background: var(--accent-teal); flex: none; }
  .brand-name {
    font-family: "Montserrat", sans-serif; font-weight: 500;
    letter-spacing: .32em; text-transform: uppercase;
    color: var(--card-white); font-size: 26px;
  }

  /* Back side */
  .card-back {
    left: 780px; top: 145px; width: 343px; height: 600px;
    background: var(--card-white);
    display: flex; flex-direction: column;
  }
  .back-logo-area { height: 318px; display: flex; align-items: center; justify-content: center; }
  .back-logo-area .brand-name { color: var(--text-dark); font-size: 17px; }
  .back-logo-area .brand-dot { width: 12px; height: 12px; }

  .name-band {
    height: 96px; background: var(--brand-blue); color: var(--card-white);
    padding: 0 34px; display: flex; flex-direction: column; justify-content: center;
  }
  .person-name { font-weight: 700; font-size: 34px; line-height: 1; text-transform: uppercase; letter-spacing: .01em; }
  .person-title { font-weight: 400; font-size: 16px; text-transform: uppercase; margin-top: 4px; }

  .contact-band {
    flex: 1; background: var(--band-dark); color: var(--text-light);
    display: flex; align-items: center; gap: 18px; padding: 0 34px;
    border-top: 1px solid var(--brand-blue);
  }
  .contact-band:first-of-type { border-top: none; }
  .contact-icon { width: 22px; height: 22px; flex: none; }
  .contact-lines { font-weight: 300; font-size: 15px; line-height: 1.3; }
</style>
</head>
<body>

  <section class="card card-front" aria-label="Card front">
    <div class="brand">
      <span class="brand-dot"></span>
      <span class="brand-name">Skylane Aerial</span>
    </div>
  </section>

  <section class="card card-back" aria-label="Card back">
    <div class="back-logo-area">
      <div class="brand">
        <span class="brand-dot"></span>
        <span class="brand-name">Skylane Aerial</span>
      </div>
    </div>

    <div class="name-band">
      <div class="person-name">Marco Reyes</div>
      <div class="person-title">Director</div>
    </div>

    <div class="contact-band">
      <svg class="contact-icon" viewBox="0 0 24 24" fill="none" stroke="currentColor" stroke-width="1.4" stroke-linejoin="round">
        <path d="M5 3h4l2 5-2.5 1.5a11 11 0 0 0 6 6L16 13l5 2v4a2 2 0 0 1-2 2A16 16 0 0 1 3 5a2 2 0 0 1 2-2z"/>
      </svg>
      <div class="contact-lines">000.5550.2184<br>000.5550.7309</div>
    </div>

    <div class="contact-band">
      <svg class="contact-icon" viewBox="0 0 24 24" fill="none" stroke="currentColor" stroke-width="1.4">
        <circle cx="12" cy="12" r="9"/>
        <ellipse cx="12" cy="12" rx="4" ry="9"/>
        <path d="M3 12h18M4.5 7.5h15M4.5 16.5h15"/>
      </svg>
      <div class="contact-lines">hello@skylaneaerial.com<br>www.skylaneaerial.com</div>
    </div>

    <div class="contact-band">
      <svg class="contact-icon" viewBox="0 0 24 24" fill="none" stroke="currentColor" stroke-width="1.4" stroke-linejoin="round">
        <path d="M12 22s7-7.2 7-12.5A7 7 0 0 0 5 9.5C5 14.8 12 22 12 22z"/>
        <circle cx="12" cy="9.5" r="2.6"/>
      </svg>
      <div class="contact-lines">42 Harbor Point<br>Surabaya, INDONESIA</div>
    </div>
  </section>

</body>
</html>
```